Vellmore Quadrant Systems LLC
Elevate Your Workflow
Vellmore Quadrant Systems LLC - Information Technology
Creative Brief
Corporate
Dorian Feltcher
President
Ashford Glen, VA
dorian@vellmore-quadrant.example
www.vellmore-quadrant.example
Elevate Your Workflow www.vellmore-quadrant.example

```html
<!DOCTYPE html>
<html lang="en">
<head>
<meta charset="utf-8">
<title>Vellmore Quadrant Systems LLC — Business Cards</title>
<link rel="stylesheet" href="https://fonts.googleapis.com/css2?family=Oswald:wght@600&family=Roboto:wght@400;700&display=swap">
<style>
  :root {
    --backdrop: #e6e7e9;
    --card-white: #ffffff;
    --card-black: #141414;
    --cyan: #35b4cf;
    --cyan-deep: #1f93ad;
    --ink: #1d1d1d;
    --ink-soft: #6b6b6b;
  }
  * { box-sizing: border-box; margin: 0; padding: 0; }
  html, body { width: 1200px; height: 982px; overflow: hidden; }
  body {
    background: var(--backdrop);
    font-family: "Roboto", Arial, sans-serif;
    color: var(--ink);
    position: relative;
  }
  .card {
    position: absolute;
    width: 510px;
    height: 292px;
    border-radius: 16px;
    box-shadow: 0 10px 26px rgba(0,0,0,.18);
    overflow: hidden;
  }
  .card--front { left: 60px; top: 120px; background: var(--card-white); }
  .card--cyan  { left: 630px; top: 120px; background: linear-gradient(160deg, #4cc3db 0%, var(--cyan) 50%, var(--cyan-deep) 100%); color: #fff; }
  .card--black { left: 60px; top: 570px; background: linear-gradient(160deg, #262626 0%, var(--card-black) 60%); color: #fff; }
  .card--white { left: 630px; top: 570px; background: var(--card-white); }

  .brand { display: flex; align-items: center; gap: 12px; }
  .brand__mark { width: 34px; height: 34px; background: var(--cyan); border-radius: 4px; flex: none; }
  .brand__name {
    font-family: "Oswald", "Arial Narrow", sans-serif;
    font-weight: 600;
    font-size: 25px;
    line-height: 1.05;
    text-transform: uppercase;
    letter-spacing: .5px;
    color: var(--ink);
  }
  .tagline { font-size: 12px; color: var(--ink-soft); }

  .card--front .brand { position: absolute; left: 32px; top: 34px; }
  .card--front .tagline { position: absolute; left: 78px; top: 100px; }
  .contact { position: absolute; left: 32px; bottom: 34px; font-size: 11.5px; line-height: 1.7; color: var(--ink-soft); }
  .contact__label { display: inline-block; width: 40px; color: var(--cyan-deep); font-weight: 700; }
  .person { position: absolute; right: 34px; top: 152px; text-align: left; }
  .person__name { font-size: 24px; color: var(--cyan-deep); font-weight: 400; }
  .person__role { font-size: 13px; color: var(--ink-soft); margin-top: 4px; }

  .back { position: absolute; inset: 0; display: flex; flex-direction: column; align-items: center; justify-content: center; }
  .back .brand__name { color: #fff; font-size: 22px; }
  .back__tagline { font-size: 13px; margin-top: 14px; opacity: .92; }
  .web { position: absolute; left: 0; right: 0; bottom: 40px; text-align: center; font-size: 12px; letter-spacing: 3px; font-weight: 700; }
  .card--black .web { color: #cfcfcf; }

  .card--white .brand { position: absolute; left: 150px; top: 86px; }
  .card--white .tagline { position: absolute; left: 196px; top: 150px; }
  .card--white .web { color: var(--ink); }
</style>
</head>
<body>
  <section class="card card--front" aria-label="Front of business card">
    <div class="brand">
      <span class="brand__mark"></span>
      <span class="brand__name">Vellmore Quadrant<br>Systems LLC</span>
    </div>
    <p class="tagline">Elevate Your Workflow</p>
    <div class="person">
      <p class="person__name">Dorian Feltcher</p>
      <p class="person__role">President</p>
    </div>
    <div class="contact">
      <p>Ashford Glen, VA</p>
      <p><span class="contact__label">Cell</span>(555) 014-2280</p>
      <p><span class="contact__label">Email</span>dorian@vellmore-quadrant.example</p>
      <p><span class="contact__label">Web</span>www.vellmore-quadrant.example</p>
    </div>
  </section>

  <section class="card card--cyan" aria-label="Back of business card, cyan">
    <div class="back">
      <div class="brand">
        <span class="brand__name">Vellmore Quadrant Systems</span>
      </div>
      <p class="back__tagline">Elevate Your Workflow</p>
    </div>
    <p class="web">www.vellmore-quadrant.example</p>
  </section>

  <section class="card card--black" aria-label="Back of business card, black">
    <div class="back">
      <div class="brand">
        <span class="brand__mark"></span>
        <span class="brand__name">Vellmore Quadrant Systems</span>
      </div>
      <p class="back__tagline">Elevate Your Workflow</p>
    </div>
    <p class="web">www.vellmore-quadrant.example</p>
  </section>

  <section class="card card--white" aria-label="Back of business card, white">
    <div class="brand">
      <span class="brand__mark"></span>
      <span class="brand__name">Vellmore Quadrant<br>Systems LLC</span>
    </div>
    <p class="tagline">Elevate Your Workflow</p>
    <p class="web">www.vellmore-quadrant.example</p>
  </section>
</body>
</html>
```